Modern Business Card For A Digital Advertising Company

I'll be print on the Tarn Prints Velour paper http://us.tarnprints.example/products/velour/business-cards.html
Need's to be modern and use the color palette of the logo or gray scales. I think integrating the pixelation of the logo in to the card and having it wrap from one side to the other could be interesting. My company provides ad operations, web development, and number of other services to websites around the world. You can see my website at http://www.pixelharbor.example
Contact info on the card needs to have
Dana Welloby
President
p.555.318.4406
dana@pixelharbor.example
http://www.pixelharbor.example
Doesn't necessarily need to be in that order
Target Market(s)
Website owners
Industry/Entity Type
Business
Look and feel

```html
<!DOCTYPE html>
<html lang="en">
<head>
<meta charset="utf-8">
<title>Pixel Harbor business card</title>
<link rel="stylesheet" href="https://fonts.googleapis.com/css2?family=PT+Sans:wght@400;700&display=swap">
<style>
  :root {
    --backdrop: #4a2a1c;
    --card: #ffffff;
    --brand-green: #8dc63f;
    --ink: #231f20;
    --ink-soft: #555555;
    --swoosh: #2b2b2b;
  }
  * { margin: 0; padding: 0; box-sizing: border-box; }
  html, body { width: 1200px; height: 448px; overflow: hidden; }
  body {
    background: var(--backdrop);
    font-family: "PT Sans", Arial, sans-serif;
    position: relative;
  }
  .card {
    position: absolute;
    top: 73px;
    width: 510px;
    height: 289px;
    border-radius: 18px;
    background: var(--card);
    overflow: hidden;
  }
  .card--front { left: 68px; }
  .card--back { left: 615px; }

  .front-shape { position: absolute; inset: 0; }

  .brand {
    position: absolute;
    left: 45px;
    top: 60px;
    color: var(--brand-green);
    font-weight: 700;
    font-size: 34px;
    line-height: 1.0;
    text-transform: uppercase;
    letter-spacing: 1px;
  }
  .brand__mark {
    width: 46px;
    height: 46px;
    background: var(--brand-green);
    margin-bottom: 12px;
  }

  .contact {
    position: absolute;
    right: 20px;
    top: 155px;
    list-style: none;
    text-align: right;
    font-size: 12.5px;
    color: var(--ink);
  }
  .contact__item {
    display: flex;
    justify-content: flex-end;
    align-items: center;
    gap: 7px;
    height: 21px;
  }
  .contact__icon { width: 11px; height: 11px; flex: none; }

  .signature {
    position: absolute;
    left: 319px;
    top: 252px;
    display: flex;
    align-items: center;
    color: var(--ink);
  }
  .signature__name { font-weight: 700; font-size: 16px; }
  .signature__rule {
    width: 1px;
    height: 18px;
    background: var(--ink);
    margin: 0 9px;
  }
  .signature__title { font-size: 12px; }

  .back-brand {
    position: absolute;
    left: 0; right: 0;
    top: 90px;
    display: flex;
    flex-direction: column;
    align-items: center;
    color: var(--brand-green);
    font-weight: 700;
    font-size: 30px;
    text-transform: uppercase;
    letter-spacing: 1px;
  }
  .back-brand__mark {
    width: 40px; height: 40px;
    background: var(--brand-green);
    margin-bottom: 10px;
  }
  .back-url {
    position: absolute;
    left: 0; right: 0;
    top: 202px;
    text-align: center;
    font-size: 11.5px;
    letter-spacing: 3px;
    color: var(--ink-soft);
  }
</style>
</head>
<body>
  <section class="card card--front">
    <svg class="front-shape" width="510" height="289" viewBox="0 0 510 289" aria-hidden="true">
      <path d="M382 0 C350 90 292 170 244 289 L510 289 L510 0 Z" fill="var(--brand-green)"/>
      <path d="M370 0 L378 0 C344 92 290 168 246 289 L238 289 C282 165 336 90 370 0 Z" fill="var(--swoosh)"/>
    </svg>

    <div class="brand">
      <div class="brand__mark"></div>
      Pixel<br>Harbor
    </div>

    <ul class="contact">
      <li class="contact__item">p.555.318.4406
        <svg class="contact__icon" viewBox="0 0 12 12" aria-hidden="true"><circle cx="6" cy="6" r="6" fill="var(--ink)"/><path d="M4 3 L5 3 L5.6 4.6 L5 5.2 Q5.8 6.6 6.8 7 L7.4 6.4 L9 7 L9 8 Q6 8.6 4 4 Z" fill="var(--brand-green)"/></svg>
      </li>
      <li class="contact__item">dana@pixelharbor.example
        <svg class="contact__icon" viewBox="0 0 12 12" aria-hidden="true"><circle cx="6" cy="6" r="6" fill="var(--ink)"/><rect x="3" y="4" width="6" height="4" fill="none" stroke="var(--brand-green)" stroke-width="0.8"/><path d="M3 4 L6 6.3 L9 4" fill="none" stroke="var(--brand-green)" stroke-width="0.8"/></svg>
      </li>
      <li class="contact__item">http://www.pixelharbor.example
        <svg class="contact__icon" viewBox="0 0 12 12" aria-hidden="true"><circle cx="6" cy="6" r="6" fill="var(--ink)"/><circle cx="6" cy="6" r="3.2" fill="none" stroke="var(--brand-green)" stroke-width="0.8"/><path d="M2.8 6 H9.2 M6 2.8 V9.2" stroke="var(--brand-green)" stroke-width="0.8"/></svg>
      </li>
    </ul>

    <div class="signature">
      <span class="signature__name">Dana Welloby</span>
      <span class="signature__rule"></span>
      <span class="signature__title">President</span>
    </div>
  </section>

  <section class="card card--back">
    <div class="back-brand">
      <div class="back-brand__mark"></div>
      Pixel Harbor
    </div>
    <p class="back-url">www.pixelharbor.example</p>
  </section>
</body>
</html>
```